Dental Office Needs Exciting New Stationary

We need a stationary design that incorporates the logo that we already have and would like to keep the existing color scheme. We need something clean and professional. This is a Endodontic (root canals) office and must represent a dental specialist's office. I need a design for a business card, envelope, and letterhead that all coordinate. I would like the business card to incorporate the information in the business card sample that I am providing. I made the business card design myself but would like to see a better one.

```html
<!DOCTYPE html>
<html lang="en">
<head>
<meta charset="utf-8">
<title>Meridian Endodontics – Stationery Set</title>
<link href="https://fonts.googleapis.com/css2?family=Montserrat:wght@400;600;700&display=swap" rel="stylesheet">
<style>
  :root{
    --backdrop:#9b9b9b;
    --paper:#ffffff;
    --brand-blue:#1a75bc;
    --brand-blue-soft:#e6eef7;
    --ink-gray:#8a8c8e;
    --ink-dark:#333740;
    --caption:#f2f2f2;
    --rule:#9ea3a8;
  }
  *{box-sizing:border-box;margin:0;padding:0}
  html,body{width:1200px;height:640px;overflow:hidden;background:var(--backdrop)}
  body{position:relative;font-family:'Montserrat',Arial,sans-serif;color:var(--ink-dark)}

  .sheet{position:absolute;background:var(--paper);box-shadow:0 3px 8px rgba(0,0,0,.35);overflow:hidden}
  .sheet--blue{background:var(--brand-blue)}

  /* brand mark: plain circle + name in one colour and weight */
  .brand{display:flex;align-items:center;gap:8px;color:var(--brand-blue);font-weight:700;line-height:1.05;letter-spacing:.04em;text-transform:uppercase}
  .brand__dot{border-radius:50%;background:currentColor;flex:none}
  .brand__name{display:block}
  .brand--white{color:#fff}

  .holder__name{color:var(--brand-blue);font-weight:700;letter-spacing:.05em;text-transform:uppercase}
  .holder__title{color:var(--ink-gray);font-weight:400;font-size:7px;letter-spacing:.05em}

  .contact{list-style:none;font-size:7px;color:var(--ink-dark)}
  .contact li{display:flex;align-items:center;gap:5px;margin-bottom:3px}
  .contact svg{width:9px;height:9px;flex:none}
  .contact--white{color:#fff}

  /* letterhead */
  .letterhead{left:36px;top:40px;width:360px;height:466px}
  .letterhead .brand{position:absolute;left:26px;top:26px;font-size:13px}
  .letterhead .brand__dot{width:18px;height:18px}
  .letterhead__holder{position:absolute;left:190px;top:30px;text-align:right;width:70px}
  .letterhead__holder .holder__name{font-size:6.5px}
  .letterhead__holder .holder__title{font-size:5px}
  .letterhead .contact{position:absolute;left:268px;top:25px;font-size:4.6px}
  .letterhead .contact li{margin-bottom:1.5px;gap:3px}
  .letterhead .contact svg{width:5px;height:5px}
  .letterhead__rule{position:absolute;left:140px;right:26px;top:66px;height:1px;background:var(--rule)}
  .letterhead__watermark{position:absolute;left:180px;top:300px;width:150px;height:150px;border-radius:50%;background:var(--brand-blue-soft)}

  /* business cards */
  .card{width:235px;height:134px}
  .card--front-a{left:430px;top:40px}
  .card--front-b{left:430px;top:190px}
  .card--back-info{left:685px;top:40px}
  .card--back-logo{left:685px;top:190px}
  .card--back-blue{left:940px;top:40px}

  .card--front-a .brand{position:absolute;left:18px;top:16px;font-size:11px}
  .card--front-a .brand__dot{width:16px;height:16px}
  .card--front-a .card__rule{position:absolute;left:0;right:60px;top:62px;height:1px;background:var(--ink-dark)}
  .card--front-a .card__holder{position:absolute;right:16px;top:52px;text-align:right}
  .card--front-a .holder__name{font-size:9px}
  .card--front-a .contact{position:absolute;left:16px;top:72px}

  .card--front-b .card__holder{position:absolute;right:16px;top:14px;text-align:right}
  .card--front-b .holder__name{font-size:9px}
  .card--front-b .card__rule{position:absolute;left:12px;right:60px;top:25px;height:1px;background:var(--ink-dark)}
  .card--front-b .contact{position:absolute;left:16px;top:32px;font-size:6px}
  .card--front-b .contact li{margin-bottom:1px}
  .card--front-b .contact svg{width:7px;height:7px}
  .card--front-b .brand{position:absolute;left:48px;top:86px;font-size:11px}
  .card--front-b .brand__dot{width:16px;height:16px}

  .card--back-info .card__decor{position:absolute;left:-20px;top:10px;width:110px;height:110px;border-radius:50%;background:rgba(255,255,255,.18)}
  .card--back-info .card__holder{position:absolute;left:140px;top:16px}
  .card--back-info .holder__name{color:#fff;font-size:8px}
  .card--back-info .holder__title{color:#fff;font-size:6px}
  .card--back-info .contact{position:absolute;left:140px;top:70px;font-size:6px}
  .card--back-info .contact li{margin-bottom:1.5px}
  .card--back-info .contact svg{width:7px;height:7px}

  .card--back-logo, .card--back-blue{display:flex;align-items:center;justify-content:center}
  .card--back-logo .brand,.card--back-blue .brand{font-size:14px;gap:10px}
  .card--back-logo .brand__dot,.card--back-blue .brand__dot{width:22px;height:22px}

  /* envelopes */
  .envelope{top:330px;width:365px;height:158px}
  .envelope--front{left:430px}
  .envelope--back{left:810px}
  .envelope--front .envelope__watermark{position:absolute;right:20px;top:12px;width:80px;height:80px;border-radius:50%;background:var(--brand-blue-soft)}
  .envelope--front .brand{position:absolute;left:18px;top:112px;font-size:10px}
  .envelope--front .brand__dot{width:14px;height:14px}
  .envelope--front .contact{position:absolute;left:190px;top:132px;display:flex;gap:14px;font-size:5px}
  .envelope--front .contact svg{width:5px;height:5px}
  .envelope__band{position:absolute;left:0;right:0;bottom:0;height:4px;background:var(--brand-blue)}
  .envelope__flap{position:absolute;inset:0;width:100%;height:100%}
  .envelope__seal{position:absolute;left:174px;top:36px;width:16px;height:16px;border-radius:50%;background:var(--brand-blue)}

  .caption{position:absolute;left:560px;top:520px;color:var(--caption);font-size:15px;line-height:1.2;font-weight:400;letter-spacing:.02em}
</style>
</head>
<body>

<svg width="0" height="0" style="position:absolute" aria-hidden="true">
  <symbol id="icon-phone" viewBox="0 0 10 10"><circle cx="5" cy="5" r="5" fill="currentColor"/><path d="M3 2.6l1 .1.4 1.2-.6.5a4 4 0 0 0 1.8 1.8l.5-.6 1.2.4.1 1-.8.6C4.6 7.4 2.6 5.4 2.4 3.4z" fill="#fff"/></symbol>
  <symbol id="icon-fax" viewBox="0 0 10 10"><circle cx="5" cy="5" r="5" fill="currentColor"/><rect x="2.6" y="4" width="4.8" height="3" fill="#fff"/><rect x="3.5" y="2.5" width="3" height="1.8" fill="#fff"/></symbol>
  <symbol id="icon-web" viewBox="0 0 10 10"><circle cx="5" cy="5" r="5" fill="currentColor"/><circle cx="5" cy="5" r="2.6" fill="none" stroke="#fff" stroke-width=".7"/><path d="M2.4 5h5.2M5 2.4v5.2" stroke="#fff" stroke-width=".6"/></symbol>
  <symbol id="icon-pin" viewBox="0 0 10 10"><circle cx="5" cy="5" r="5" fill="currentColor"/><path d="M5 2.2a2 2 0 0 1 2 2c0 1.5-2 3.6-2 3.6S3 5.7 3 4.2a2 2 0 0 1 2-2z" fill="#fff"/><circle cx="5" cy="4.2" r=".7" fill="currentColor"/></symbol>
</svg>

<!-- Letterhead -->
<section class="sheet letterhead" aria-label="Letterhead">
  <div class="brand"><span class="brand__dot"></span><span class="brand__name">Meridian<br>Endodontics</span></div>
  <div class="letterhead__holder"><div class="holder__name">Daniel R Whitcomb</div><div class="holder__title">DDS MS</div></div>
  <ul class="contact" style="color:var(--brand-blue)">
    <li><svg><use href="#icon-phone"/></svg><span style="color:var(--ink-dark)">555.210.4471</span></li>
    <li><svg><use href="#icon-fax"/></svg><span style="color:var(--ink-dark)">555.210.4480</span></li>
    <li><svg><use href="#icon-web"/></svg><span style="color:var(--ink-dark)">www.meridianendo.com</span></li>
    <li><svg><use href="#icon-pin"/></svg><span style="color:var(--ink-dark)">480 Alder Avenue, Riverton, CA 95000</span></li>
  </ul>
  <div class="letterhead__rule"></div>
  <div class="letterhead__watermark"></div>
</section>

<!-- Business card front A -->
<section class="sheet card card--front-a" aria-label="Business card front">
  <div class="brand"><span class="brand__dot"></span><span class="brand__name">Meridian<br>Endodontics</span></div>
  <div class="card__rule"></div>
  <div class="card__holder"><div class="holder__name">Daniel R Whitcomb</div><div class="holder__title">DDS MS</div></div>
  <ul class="contact" style="color:var(--brand-blue)">
    <li><svg><use href="#icon-phone"/></svg><span style="color:var(--ink-dark)">555.210.4471</span></li>
    <li><svg><use href="#icon-fax"/></svg><span style="color:var(--ink-dark)">555.210.4480</span></li>
    <li><svg><use href="#icon-web"/></svg><span style="color:var(--ink-dark)">www.meridianendo.com</span></li>
    <li><svg><use href="#icon-pin"/></svg><span style="color:var(--ink-dark)">480 Alder Avenue, Riverton, CA 95000</span></li>
  </ul>
</section>

<!-- Business card front B -->
<section class="sheet card card--front-b" aria-label="Business card front, alternate">
  <div class="card__holder"><div class="holder__name">Daniel R Whitcomb</div><div class="holder__title">DDS MS</div></div>
  <div class="card__rule"></div>
  <ul class="contact" style="color:var(--brand-blue)">
    <li><svg><use href="#icon-phone"/></svg><span style="color:var(--ink-dark)">555.210.4471</span></li>
    <li><svg><use href="#icon-fax"/></svg><span style="color:var(--ink-dark)">555.210.4480</span></li>
    <li><svg><use href="#icon-web"/></svg><span style="color:var(--ink-dark)">www.meridianendo.com</span></li>
    <li><svg><use href="#icon-pin"/></svg><span style="color:var(--ink-dark)">480 Alder Avenue, Riverton, CA 95000</span></li>
  </ul>
  <div class="brand"><span class="brand__dot"></span><span class="brand__name">Meridian<br>Endodontics</span></div>
</section>

<!-- Business card back, blue with details -->
<section class="sheet sheet--blue card card--back-info" aria-label="Business card back with details">
  <div class="card__decor"></div>
  <div class="card__holder"><div class="holder__name">Daniel R Whitcomb</div><div class="holder__title">DDS MS</div></div>
  <ul class="contact contact--white" style="color:rgba(255,255,255,.25)">
    <li><svg><use href="#icon-phone"/></svg><span style="color:#fff">555.210.4471</span></li>
    <li><svg><use href="#icon-fax"/></svg><span style="color:#fff">555.210.4480</span></li>
    <li><svg><use href="#icon-web"/></svg><span style="color:#fff">www.meridianendo.com</span></li>
    <li><svg><use href="#icon-pin"/></svg><span style="color:#fff">480 Alder Avenue, Riverton, CA 95000</span></li>
  </ul>
</section>

<!-- Business card back, white logo -->
<section class="sheet card card--back-logo" aria-label="Business card back">
  <div class="brand"><span class="brand__dot"></span><span class="brand__name">Meridian<br>Endodontics</span></div>
</section>

<!-- Business card back, blue logo -->
<section class="sheet sheet--blue card card--back-blue" aria-label="Business card back, blue">
  <div class="brand brand--white"><span class="brand__dot"></span><span class="brand__name">Meridian<br>Endodontics</span></div>
</section>

<!-- Envelope front -->
<section class="sheet envelope envelope--front" aria-label="Envelope front">
  <div class="envelope__watermark"></div>
  <div class="brand"><span class="brand__dot"></span><span class="brand__name">Meridian<br>Endodontics</span></div>
  <ul class="contact" style="color:var(--brand-blue)">
    <li><svg><use href="#icon-web"/></svg><span style="color:var(--ink-dark)">www.meridianendo.com</span></li>
    <li><svg><use href="#icon-pin"/></svg><span style="color:var(--ink-dark)">480 Alder Avenue, Riverton, CA 95000</span></li>
  </ul>
  <div class="envelope__band"></div>
</section>

<!-- Envelope back -->
<section class="sheet envelope envelope--back" aria-label="Envelope back">
  <svg class="envelope__flap" viewBox="0 0 365 158" preserveAspectRatio="none" aria-hidden="true">
    <path d="M6 4 Q6 66 40 70 L325 70 Q359 66 359 4" fill="none" stroke="#c9ccd0" stroke-width="1"/>
  </svg>
  <div class="envelope__seal"></div>
</section>

<p class="caption">Letterhead<br>Business Card 2 front 3 back<br>Envelope front and Back</p>

</body>
</html>
```